Beautiful Quotes For Social Media Posts

We are looking for 5 beautifully designed quotes for our social media account.

Inspiration of styles we like in both style and color along with a few of our favorite fonts (you are NOT limited to these fonts this is just to give you an idea):
https://quillmorestudio.example.com/s/k7p2vx9tqa41mzn8wbd3ce6hr5lf0y2j

*These fonts are property of Quillmore Studio. You do not have permission/rights to use them outside of this assignment*

Quotes to use (5):
“Only those who dare to fail greatly can ever achieve greatly.” –Vernon T. Ashgrove
“Don’t go through life, grow through life.” – Milo Pendrake
“Follow your bliss and the universe will open doors where there were only walls.” – Arthur Venholm
“If you don’t like the road you’re walking, start paving another one.” – Greta Mossley
“Life is like riding a bicycle. To keep your balance, you must keep moving.” —Lucian Thornwick

File Specifics:
- JPG
- 10x10 in size (square)
- Please include @QuillmoreStudio in the bottom right left or center of each design

Brand Details:
Soft but rich pastel and bright colors.
Hand Drawn florals, doodles and art
Handwritten looking fonts
Artsy, Creative, Girl and Inspiring

```html
<!DOCTYPE html>
<html lang="en">
<head>
<meta charset="utf-8">
<title>Quote Posts – Quillmore Studio</title>
<link rel="stylesheet" href="https://fonts.googleapis.com/css2?family=Allura&family=Amatic+SC:wght@700&family=Boogaloo&family=Great+Vibes&family=Kaushan+Script&family=Poppins:wght@400&family=Righteous&family=Yellowtail&display=swap">
<style>
  :root {
    --board: #58575a;
    --coral: #ec7465;
    --coral-deep: #d4544a;
    --coral-leaf: #f4a79c;
    --cream: #fde9e0;
    --blush: #fdf0ea;
    --tan: #d38e6a;
    --brick: #c9473c;
    --wine: #a8141f;
    --ink: #111111;
    --gold: #e3ae3f;
    --gold-line: #f7c99a;
    --rose: #e3305e;
    --rose-deep: #cc0f4e;
    --sun: #ffe600;
    --petal: #fbe6ec;
    --magenta: #e0137f;
    --white: #ffffff;
  }
  * { box-sizing: border-box; margin: 0; padding: 0; }
  html, body { width: 876px; height: 1200px; overflow: hidden; }
  body { background: var(--board); position: relative; font-family: "Poppins", sans-serif; }

  .post { position: absolute; width: 334px; height: 334px; overflow: hidden; box-shadow: 0 4px 10px rgba(0,0,0,.35); }
  .post > * { position: absolute; }
  .handle { font-family: "Poppins", sans-serif; font-size: 8.5px; text-align: center; line-height: 1; }

  /* Post 1 – dare to fail */
  .post-dare { left: 83px; top: 55px; background: var(--coral); }
  .post-dare .foliage { inset: 0; background: radial-gradient(circle at 50% 50%, transparent 55%, var(--coral-leaf) 80%, #f59a6f 100%); opacity: .8; }
  .post-dare .medallion { left: 18px; top: 18px; width: 298px; height: 298px; border-radius: 50%; background: var(--coral-deep); }
  .post-dare .ring { left: 10px; top: 8px; width: 314px; height: 318px; border-radius: 50%; border: 1px solid rgba(255,255,255,.8); }
  .post-dare .quote { left: 0; width: 100%; top: 48px; text-align: center; color: var(--white); font-family: "Boogaloo", sans-serif; line-height: .95; }
  .post-dare .lead { font-family: "Allura", cursive; font-size: 34px; display: block; margin-bottom: 6px; }
  .post-dare .big { font-size: 50px; display: block; }
  .post-dare .small { font-size: 26px; display: block; margin: 2px 0; }
  .post-dare .author { left: 0; width: 100%; top: 262px; text-align: center; color: var(--white); font-family: "Allura", cursive; font-size: 22px; }

  /* Post 2 – grow through life */
  .post-grow { left: 460px; top: 55px; background: var(--coral); }
  .post-grow .panel { left: 33px; top: 33px; width: 268px; height: 268px; background: var(--blush); }
  .post-grow .frame { left: 22px; top: 52px; width: 296px; height: 240px; border: 1.5px solid var(--gold-line); transform: rotate(-4deg); }
  .post-grow .lily-top { left: 0; top: 0; width: 170px; height: 70px; background: radial-gradient(ellipse at 40% 30%, #ffffff 0%, #f3e6e1 60%, transparent 75%); }
  .post-grow .lily-bottom { right: 0; bottom: 0; width: 80px; height: 170px; background: radial-gradient(ellipse at 60% 60%, #ffffff 0%, #f3e6e1 60%, transparent 78%); }
  .post-grow .quote { left: 40px; width: 260px; top: 55px; text-align: center; font-family: "Great Vibes", cursive; color: var(--wine); line-height: 1; }
  .post-grow .dont { display: block; font-size: 60px; color: var(--ink); margin-left: 20px; }
  .post-grow .line { display: block; font-size: 40px; }
  .post-grow .life { display: block; font-size: 44px; color: var(--ink); margin-left: -40px; }
  .post-grow .author { left: 120px; top: 264px; font-family: "Righteous", sans-serif; font-size: 12px; color: var(--wine); }
  .post-grow .handle { left: 0; width: 100%; top: 314px; color: var(--white); }

  /* Post 3 – follow your bliss */
  .post-bliss { left: 83px; top: 433px; background: var(--cream); }
  .post-bliss .rule { left: 18px; top: 17px; width: 298px; height: 298px; border: 1px solid var(--brick); }
  .post-bliss .panel { left: 26px; top: 25px; width: 283px; height: 283px; background: var(--tan); }
  .post-bliss .bloom-top { right: 0; top: 0; width: 115px; height: 150px; background: radial-gradient(ellipse at 65% 35%, #f08a72 0%, #f6c2b0 50%, transparent 75%); }
  .post-bliss .bloom-bottom { left: 0; bottom: 0; width: 170px; height: 175px; background: radial-gradient(ellipse at 30% 65%, #f29b83 0%, #f8cdbd 50%, transparent 75%); }
  .post-bliss .quote { left: 30px; width: 280px; top: 44px; text-align: center; font-family: "Amatic SC", sans-serif; font-weight: 700; font-size: 40px; line-height: 33px; color: var(--blush); text-shadow: 2px 2px 0 #3a2a24; }
  .post-bliss .accent { color: var(--brick); text-shadow: 1px 1px 0 #f5d1c4; }
  .post-bliss .author { left: 110px; top: 232px; font-family: "Amatic SC", sans-serif; font-weight: 700; font-size: 28px; line-height: 1; color: var(--ink); }
  .post-bliss .handle { left: 210px; top: 264px; color: var(--blush); }

  /* Post 4 – pave another road */
  .post-road { left: 460px; top: 433px; background: var(--rose); }
  .post-road .pattern { inset: 0; background: radial-gradient(circle at 80% 10%, rgba(255,255,255,.9) 0 14%, transparent 15%), radial-gradient(circle at 20% 92%, rgba(255,255,255,.9) 0 14%, transparent 15%), radial-gradient(circle at 45% 10%, var(--gold) 0 12%, transparent 13%), radial-gradient(circle at 62% 92%, var(--gold) 0 10%, transparent 11%); }
  .post-road .frame { left: 14px; top: 69px; width: 305px; height: 197px; background: var(--gold); }
  .post-road .mat { left: 20px; top: 75px; width: 293px; height: 185px; background: var(--white); }
  .post-road .card { left: 25px; top: 80px; width: 283px; height: 175px; background: radial-gradient(circle at 50% 40%, #e83168, var(--rose-deep)); }
  .post-road .quote { left: 25px; width: 283px; top: 90px; text-align: center; font-family: "Kaushan Script", cursive; color: var(--white); font-size: 21px; line-height: 1.45; }
  .post-road .author { left: 0; width: 100%; top: 198px; text-align: center; font-family: "Kaushan Script", cursive; color: var(--sun); font-size: 16px; }
  .post-road .divider { left: 61px; top: 229px; width: 213px; height: 1px; background: var(--gold); }
  .post-road .handle { left: 0; width: 100%; top: 237px; color: var(--ink); }

  /* Post 5 – riding a bicycle */
  .post-cycle { left: 275px; top: 808px; background: var(--petal); }
  .post-cycle .watercolour { inset: 0; background: radial-gradient(circle at 10% 10%, #6fa6a0 0, transparent 30%), radial-gradient(circle at 90% 85%, #5c4a5c 0, transparent 28%), radial-gradient(circle at 95% 40%, #8fc08c 0, transparent 22%), radial-gradient(circle at 15% 90%, #6fa6a0 0, transparent 25%); opacity: .7; }
  .post-cycle .disc { left: 13px; top: 14px; width: 308px; height: 308px; border-radius: 50%; background: radial-gradient(circle, #fbeef2 60%, #eadde2 100%); box-shadow: 0 2px 8px rgba(0,0,0,.15); }
  .post-cycle .quote { left: 0; width: 100%; top: 58px; text-align: center; font-family: "Kaushan Script", cursive; line-height: 1.15; }
  .post-cycle .lead { display: block; color: var(--magenta); font-size: 36px; }
  .post-cycle .rest { display: block; color: var(--ink); font-size: 22px; margin-top: 4px; }
  .post-cycle .author { left: 0; width: 100%; top: 232px; text-align: center; font-family: "Kaushan Script", cursive; color: var(--magenta); font-size: 16px; }
  .post-cycle .handle { left: 0; width: 100%; top: 256px; color: var(--ink); }
</style>
</head>
<body>

<section class="post post-dare">
  <div class="foliage" role="img" aria-label="Pastel tropical palm leaves and dots around the edges"></div>
  <div class="medallion"></div>
  <div class="ring"></div>
  <p class="quote"><span class="lead">“Only those</span><span class="big">WHO DARE</span><span class="small">TO FAIL GREATLY</span><span class="big">CAN EVER</span><span class="small">ACHIEVE GREATLY.”</span></p>
  <p class="author">–Vernon T. Ashgrove</p>
</section>

<section class="post post-grow">
  <div class="panel"></div>
  <div class="frame"></div>
  <div class="lily-top" role="img" aria-label="Line-drawn lily flowers in the top left corner"></div>
  <div class="lily-bottom" role="img" aria-label="Line-drawn lily flowers in the bottom right corner"></div>
  <p class="quote"><span class="dont">“Don’t</span><span class="line">go through life,</span><span class="line">grow through”</span><span class="life">life.</span></p>
  <p class="author">_ Milo Pendrake</p>
  <p class="handle">@QuillmoreStudio</p>
</section>

<section class="post post-bliss">
  <div class="rule"></div>
  <div class="panel"></div>
  <div class="bloom-top" role="img" aria-label="Watercolour peach flowers and green leaves, top right"></div>
  <div class="bloom-bottom" role="img" aria-label="Watercolour peach flowers and green leaves, bottom left"></div>
  <p class="quote">“Follow your bliss<br>and the universe<br><span class="accent">will open doors<br>where there</span><br>were only walls.”</p>
  <p class="author">— Arthur Venholm</p>
  <p class="handle">@QuillmoreStudio</p>
</section>

<section class="post post-road">
  <div class="pattern" role="img" aria-label="Bold white and gold organic blob pattern on pink"></div>
  <div class="frame"></div>
  <div class="mat"></div>
  <div class="card"></div>
  <p class="quote">If you don’t like<br>the road you’re walking,<br>start paving another one</p>
  <p class="author">– Greta Mossley</p>
  <div class="divider"></div>
  <p class="handle">@QuillmoreStudio</p>
</section>

<section class="post post-cycle">
  <div class="watercolour" role="img" aria-label="Watercolour and ink floral background in teal, pink and plum"></div>
  <div class="disc"></div>
  <p class="quote"><span class="lead">“Life is like<br>riding a bicycle.</span><span class="rest">To keep your balance,<br>you must keep moving.”</span></p>
  <p class="author">–Lucian Thornwick</p>
  <p class="handle">@QuillmoreStudio</p>
</section>

</body>
</html>
```